Marketing folder with booklet and brochure. Slot for business card

We are a dual-branded commercial and residential flooring installation company. Carpet, resilient, wood, tile, flooring repairs, sand and finish wood. We like designs using red, white, and blue. Custom Font style is Luna Bar, available upon request Content available on our website qendwick-surfaces.net. Ideally would like a small booklet of services, letterhead for intro letter, folder, and possibly tri-fold.

Target Market(s)

Builders, designers, and contractors. We do not typically work for the general public

Industry/Entity Type

Construction

Contact Information for Business Card

We currently have business cards, but because we want a card slot in the folder, we might have to match toward our print package. Check out our web site qendwick-surfaces.net

Font styles to use
Serif

Colors
0456a4
ec1f27
ffffff

```html
<!DOCTYPE html>
<html lang="en">
<head>
<meta charset="utf-8">
<title>Qendwick Surfaces — Letterhead</title>
<link rel="stylesheet" href="https://fonts.googleapis.com/css2?family=Questrial&display=swap">
<style>
  :root {
    --brand-blue: #0456a4;
    --brand-red: #ec1f27;
    --paper: #ffffff;
    --ink: #111111;
    --wash-blue: #e6eef7;
  }
  * { margin: 0; padding: 0; box-sizing: border-box; }
  html, body {
    width: 848px;
    height: 1200px;
    overflow: hidden;
    background: var(--paper);
  }
  .letterhead {
    position: relative;
    width: 848px;
    height: 1200px;
    overflow: hidden;
    background: var(--paper);
    font-family: "Questrial", "Century Gothic", sans-serif;
    color: var(--ink);
  }
  .brand-name {
    position: absolute;
    left: 28px;
    top: 70px;
    font-size: 40px;
    letter-spacing: 1px;
    line-height: 1;
    color: var(--brand-blue);
    white-space: nowrap;
  }
  .sender-address {
    position: absolute;
    left: 572px;
    top: 71px;
    font-size: 16px;
    line-height: 21px;
    font-style: normal;
    color: var(--ink);
  }
  .brand-wash {
    position: absolute;
    left: 10px;
    top: 800px;
    font-size: 240px;
    line-height: 1;
    letter-spacing: 4px;
    color: var(--wash-blue);
    white-space: nowrap;
    pointer-events: none;
  }
  .footer-rule {
    position: absolute;
    left: 93px;
    top: 1146px;
    width: 653px;
    height: 2px;
  }
  .footer-note {
    position: absolute;
    left: 0;
    width: 834px;
    top: 1154px;
    text-align: center;
    font-size: 15px;
    color: var(--ink);
  }
</style>
</head>
<body>
  <div class="letterhead">
    <div class="brand-name">QENDWICK SURFACES</div>

    <address class="sender-address">
      2750 Larchmere Ave NE #210,<br>
      Brookhaven MN 55990<br>
      555.014.2786
    </address>

    <div class="brand-wash" aria-hidden="true">QENDWICK</div>

    <svg class="footer-rule" viewBox="0 0 653 2" preserveAspectRatio="none" aria-hidden="true">
      <defs>
        <linearGradient id="ruleFade" x1="0" x2="1" y1="0" y2="0">
          <stop offset="0" stop-color="#111" stop-opacity="0"/>
          <stop offset="0.15" stop-color="#111" stop-opacity="1"/>
          <stop offset="0.85" stop-color="#111" stop-opacity="1"/>
          <stop offset="1" stop-color="#111" stop-opacity="0"/>
        </linearGradient>
      </defs>
      <rect x="0" y="0" width="653" height="1.4" fill="url(#ruleFade)"/>
    </svg>

    <div class="footer-note">Bankers</div>
  </div>
</body>
</html>
```